Lumavera Packaging Design Project Hair Removal products

Lumavera is launching a New Hair Removal Sub Brand, under the Lumavera Brand .

This new hair removal range will include approx six products that are all designed to remove hair. These include hot wax, wax strips, depilitaory creams, hair removal lotion etc.

We are looking for a fresh new look and a sub brand name for the range. Currently we have a name Lumavera Presto Glidea as a name option but we are not sold on this name so we would like to see other options . We would like the brand to use the same primary colours as our current lumavera brand. ie the pink and the blue but it should look different from the current range. I will email through all the pantones and logos on the brand. You can check out lumavera.co.za to see the current range

For the design we would like to see a design for a sticker that goes on a bottle as well as see how it translates on a box.

Target Market(s)

any female using hair removal products

Industry/Entity Type

Hair

Requirements
Must have
• simple design.

must use our colours

it must somehow portray that using our hair removal system is really quick, easy and effective

You can use images of legs on the packaging but it is not required.

all design must have the main brand logo "Lumavera" on the packaging but with regard to the sub name for the brand we are not sold on our name so we require that for one of your artwork options that you use our name "Presto Glidea" for one of the designs , however we would also like you to come up with your own name for the hair removal range.

Lumavera logo is not dominant and can remain in the background.

```html
<!DOCTYPE html>
<html lang="en">
<head>
<meta charset="utf-8">
<title>Lumavera Presto Glidea – Box Dieline</title>
<link href="https://fonts.googleapis.com/css2?family=Quicksand:wght@300;400;500&display=swap" rel="stylesheet">
<style>
  :root {
    --pink: #ec4b8c;
    --pink-deep: #e23a7e;
    --pink-soft: #f7a9c8;
    --white: #ffffff;
    --flap-line: #e3e3e3;
    --bg-center: #fafafa;
    --bg-edge: #c9cacc;
    --text-pink: #e8458a;
  }
  html, body {
    margin: 0;
    padding: 0;
    width: 1200px;
    height: 901px;
    overflow: hidden;
  }
  body {
    background: radial-gradient(ellipse at 45% 40%, var(--bg-center) 0%, #e9e9ea 55%, var(--bg-edge) 100%);
    font-family: "Quicksand", sans-serif;
    position: relative;
  }
  .dieline {
    position: absolute;
    left: 0;
    top: 0;
    width: 1200px;
    height: 901px;
  }
  .panel {
    position: absolute;
    left: 216px;
    width: 393px;
    height: 144px;
    background: var(--white);
    box-shadow: 0 0 0 1px var(--flap-line);
    overflow: hidden;
  }
  .panel-a { top: 96px; }
  .panel-b { top: 240px; }
  .panel-c { top: 384px; }
  .panel-d { top: 528px; }

  .brand-mark {
    position: absolute;
    left: 24px;
    top: 20px;
    display: flex;
    align-items: center;
    gap: 6px;
    color: var(--text-pink);
    font-size: 16px;
    font-weight: 400;
    letter-spacing: 0.3px;
  }
  .brand-mark .dot {
    width: 8px;
    height: 8px;
    border-radius: 50%;
    background: var(--pink);
  }
  .product-name {
    position: absolute;
    left: 20px;
    top: 62px;
    color: var(--text-pink);
    font-size: 36px;
    font-weight: 300;
    line-height: 1;
    white-space: nowrap;
  }
  .descriptor {
    position: absolute;
    left: 168px;
    top: 106px;
    color: var(--text-pink);
    font-size: 11px;
    font-weight: 500;
  }
  .rule {
    position: absolute;
    left: 0;
    bottom: 8px;
    width: 100%;
    height: 3px;
    background: var(--pink);
  }
  .photo {
    position: absolute;
    top: 0;
    right: 0;
    width: 150px;
    height: 136px;
    background: linear-gradient(135deg, rgba(255,255,255,0) 0%, var(--pink-soft) 40%, var(--pink-deep) 100%);
  }
  .panel-b .photo, .panel-d .photo {
    width: 130px;
    right: 12px;
    background: linear-gradient(160deg, rgba(255,255,255,0) 0%, var(--pink-soft) 45%, var(--pink) 100%);
  }

  .side-tab {
    position: absolute;
    background: var(--pink);
    display: flex;
    align-items: center;
    justify-content: center;
  }
  .side-tab-right {
    left: 609px;
    top: 100px;
    width: 106px;
    height: 136px;
    border-radius: 0 10px 10px 0;
  }
  .side-tab-left {
    left: 46px;
    top: 388px;
    width: 170px;
    height: 136px;
    border-radius: 10px 0 0 10px;
  }
  .side-tab .brand-vertical {
    color: var(--white);
    font-size: 16px;
    font-weight: 400;
    transform: rotate(90deg);
    white-space: nowrap;
    display: flex;
    align-items: center;
    gap: 6px;
  }
  .side-tab .brand-vertical .dot {
    width: 8px;
    height: 8px;
    border-radius: 50%;
    background: var(--white);
  }

  .dust-flap {
    position: absolute;
    background: var(--white);
    width: 102px;
    height: 140px;
    filter: drop-shadow(0 0 1px #cfcfcf);
  }
  .dust-flap-left {
    left: 114px;
    clip-path: polygon(40% 0, 100% 0, 100% 100%, 0 100%, 0 12%);
  }
  .dust-flap-right {
    left: 609px;
    clip-path: polygon(0 0, 60% 0, 100% 12%, 100% 100%, 0 100%);
  }
  .flap-b { top: 242px; }
  .flap-d { top: 530px; }

  .top-tuck {
    position: absolute;
    left: 230px;
    top: 84px;
    width: 365px;
    height: 12px;
    background: var(--white);
    border-radius: 8px 8px 0 0;
    box-shadow: 0 0 0 1px var(--flap-line);
  }
  .bottom-flap {
    position: absolute;
    left: 216px;
    top: 672px;
    width: 393px;
    height: 38px;
    background: var(--pink);
    clip-path: polygon(0 0, 100% 0, 97% 100%, 3% 100%);
  }
</style>
</head>
<body>
  <div class="dieline">
    <div class="top-tuck"></div>

    <div class="dust-flap dust-flap-left flap-b"></div>
    <div class="dust-flap dust-flap-right flap-b"></div>
    <div class="dust-flap dust-flap-left flap-d"></div>
    <div class="dust-flap dust-flap-right flap-d"></div>

    <section class="panel panel-a">
      <div class="photo" role="img" aria-label="Photo of slim legs in a flowing pink dress"></div>
      <div class="brand-mark"><span>Lumavera</span><span class="dot"></span></div>
      <div class="product-name">Presto Glidea</div>
      <div class="descriptor">hair removal</div>
      <div class="rule"></div>
    </section>

    <div class="side-tab side-tab-right">
      <div class="brand-vertical"><span>Lumavera</span><span class="dot"></span></div>
    </div>

    <section class="panel panel-b">
      <div class="photo" role="img" aria-label="Photo of a woman in a flowing pink dress"></div>
      <div class="brand-mark"><span>Lumavera</span><span class="dot"></span></div>
      <div class="product-name">Presto Glidea</div>
      <div class="descriptor">hair removal</div>
      <div class="rule"></div>
    </section>

    <div class="side-tab side-tab-left">
      <div class="brand-vertical"><span>Lumavera</span><span class="dot"></span></div>
    </div>

    <section class="panel panel-c">
      <div class="photo" role="img" aria-label="Photo of slim legs in a flowing pink dress"></div>
      <div class="brand-mark"><span>Lumavera</span><span class="dot"></span></div>
      <div class="product-name">Presto Glidea</div>
      <div class="descriptor">hair removal</div>
      <div class="rule"></div>
    </section>

    <section class="panel panel-d">
      <div class="photo" role="img" aria-label="Photo of a woman in a flowing pink dress"></div>
      <div class="brand-mark"><span>Lumavera</span><span class="dot"></span></div>
      <div class="product-name">Presto Glidea</div>
      <div class="descriptor">hair removal</div>
      <div class="rule"></div>
    </section>

    <div class="bottom-flap"></div>
  </div>
</body>
</html>
```